VERIDAX Need a luxury modern business card designed.

Need a luxury modern business card designed. refer to the uploaded files for the company name and logo in the zip file under source files. i will making my descion on monday. so please send in before then so if we need to edit we will have the time. we have a trade show coming up and im on a deadline for printer.

Target Market(s)

high end clients

Contact Information for Business Card

Company nAme and logo. Calvin Ostrow Co-Founder / Project Manager Office # 416-555-0193 Cell # 416-555-0147 VERIDAX.CA Calvin@veridax.ca

Font styles to use
Other font styles liked:
• Modern

Requirements
Must have
• Company name and logo, contact info, using the black, gold and white color scheme.

```html
<!DOCTYPE html>
<html lang="en">
<head>
<meta charset="utf-8">
<title>VERIDAX Business Card</title>
<link rel="stylesheet" href="https://fonts.googleapis.com/css2?family=Didact+Gothic&display=swap">
<style>
  :root {
    --backdrop: #8d8d8d;
    --card-white: #eef0f0;
    --card-black: #1c1d1e;
    --gold: #8a7a35;
    --text-dark: #3a3a3a;
    --text-light: #f2f2f2;
  }
  * { margin: 0; padding: 0; box-sizing: border-box; }
  html, body {
    width: 1200px;
    height: 787px;
    overflow: hidden;
    background: var(--backdrop);
    font-family: "Didact Gothic", "Century Gothic", sans-serif;
  }
  .stage {
    width: 1200px;
    height: 787px;
    display: flex;
    align-items: center;
    justify-content: center;
    gap: 40px;
  }
  .card {
    position: relative;
    width: 520px;
    height: 297px;
    overflow: hidden;
  }
  .card--front { background: var(--card-white); }
  .card--back  { background: var(--card-black); }

  .edge-band {
    position: absolute;
    left: 0;
    top: 0;
    width: 14px;
    height: 100%;
    background: var(--gold);
  }
  .contact-block {
    position: absolute;
    left: 300px;
    top: 92px;
    color: var(--text-dark);
    letter-spacing: 0.06em;
  }
  .contact-name { font-size: 19px; line-height: 1.1; }
  .contact-role { font-size: 14px; line-height: 1.2; }
  .contact-address { font-size: 14px; margin-top: 20px; }
  .contact-list {
    list-style: none;
    margin-top: 16px;
    font-size: 14px;
    line-height: 1.45;
  }
  .contact-list li { display: flex; align-items: center; gap: 8px; }
  .contact-icon { width: 11px; height: 11px; fill: var(--text-dark); flex: none; }

  .brand {
    position: absolute;
    inset: 0;
    display: flex;
    flex-direction: column;
    align-items: center;
    justify-content: center;
    color: var(--text-light);
  }
  .brand-mark {
    width: 22px;
    height: 22px;
    background: var(--gold);
    margin-bottom: 16px;
  }
  .brand-name {
    font-size: 38px;
    letter-spacing: 0.28em;
    padding-left: 0.28em;
    line-height: 1;
  }
</style>
</head>
<body>
<main class="stage">
  <section class="card card--front" aria-label="Business card front">
    <span class="edge-band" aria-hidden="true"></span>
    <div class="contact-block">
      <p class="contact-name">Name Name</p>
      <p class="contact-role">Owner</p>
      <p class="contact-address">Address</p>
      <ul class="contact-list">
        <li>
          <svg class="contact-icon" viewBox="0 0 24 24" aria-hidden="true"><path d="M6.6 10.8a15.1 15.1 0 0 0 6.6 6.6l2.2-2.2a1 1 0 0 1 1-.25 11.4 11.4 0 0 0 3.6.57 1 1 0 0 1 1 1V20a1 1 0 0 1-1 1A17 17 0 0 1 3 4a1 1 0 0 1 1-1h3.5a1 1 0 0 1 1 1c0 1.25.2 2.45.57 3.57a1 1 0 0 1-.25 1z"/></svg>
          <span>000 0000 0000</span>
        </li>
        <li>
          <svg class="contact-icon" viewBox="0 0 24 24" aria-hidden="true"><path d="M2 5h20v14H2zm2 2v.5l8 5 8-5V7zm0 2.9V17h16V9.9l-8 5z"/></svg>
          <span>info@veridax.com</span>
        </li>
        <li>
          <svg class="contact-icon" viewBox="0 0 24 24" aria-hidden="true"><circle cx="12" cy="12" r="9" fill="none" stroke="var(--text-dark)" stroke-width="2"/><path d="M3 12h18M12 3v18" stroke="var(--text-dark)" stroke-width="1.6"/></svg>
          <span>www.veridax.com</span>
        </li>
      </ul>
    </div>
  </section>

  <section class="card card--back" aria-label="Business card back">
    <div class="brand">
      <span class="brand-mark" aria-hidden="true"></span>
      <p class="brand-name">VERIDAX</p>
    </div>
  </section>
</main>
</body>
</html>
```